Veltrano - Mechanic/Collision Center Business Card

We're looking for a business card design for our mechanic/ collision repair shop.

Can be with colours or monochromatic.

See the attached files.

Many thanks

```html
<!DOCTYPE html>
<html lang="en">
<head>
<meta charset="utf-8">
<title>Veltrano – Business Card</title>
<link href="https://fonts.googleapis.com/css2?family=Exo+2:wght@400;500;700;800;900&display=swap" rel="stylesheet">
<style>
  :root {
    --backdrop: #e9e6e1;
    --brand-blue: #12729f;
    --steel-grey: #5f6166;
    --text-grey: #4a4c50;
    --card-white: #ffffff;
  }
  * { margin: 0; padding: 0; box-sizing: border-box; }
  html, body { width: 1200px; height: 900px; overflow: hidden; }
  body {
    background: var(--backdrop);
    font-family: "Exo 2", sans-serif;
    position: relative;
  }
  .card {
    position: absolute;
    left: 311px;
    width: 576px;
    height: 329px;
    overflow: hidden;
  }
  .card-front {
    top: 98px;
    background: var(--brand-blue);
    display: flex;
    align-items: center;
    justify-content: center;
  }
  .front-wordmark {
    color: var(--card-white);
    font-weight: 900;
    font-size: 62px;
    letter-spacing: 2px;
    text-transform: uppercase;
  }
  .card-back {
    top: 472px;
    background: var(--card-white);
  }
  .back-graphic {
    position: absolute;
    inset: 0;
  }
  .back-details {
    position: absolute;
    left: 30px;
    top: 0;
    width: 300px;
  }
  .back-wordmark {
    position: absolute;
    top: 72px;
    left: 0;
    color: var(--brand-blue);
    font-weight: 900;
    font-size: 34px;
    letter-spacing: 1px;
    text-transform: uppercase;
  }
  .person-name {
    position: absolute;
    top: 131px;
    color: var(--text-grey);
    font-weight: 700;
    font-size: 18px;
    letter-spacing: 0.5px;
  }
  .person-role {
    position: absolute;
    top: 150px;
    color: var(--brand-blue);
    font-weight: 500;
    font-size: 12px;
  }
  .address {
    position: absolute;
    top: 172px;
    color: var(--brand-blue);
    font-size: 14.5px;
    line-height: 19px;
  }
  .contact-list {
    position: absolute;
    top: 220px;
    list-style: none;
  }
  .contact-list li {
    display: flex;
    align-items: center;
    height: 22.5px;
    color: var(--text-grey);
    font-size: 14.5px;
  }
  .contact-icon {
    width: 18px;
    height: 18px;
    margin-right: 8px;
    fill: var(--brand-blue);
    flex: none;
  }
  .social-square {
    width: 17px;
    height: 17px;
    margin-right: 9px;
    background: var(--brand-blue);
    border-radius: 2px;
    flex: none;
  }
</style>
</head>
<body>

<section class="card card-front">
  <span class="front-wordmark">Veltrano</span>
</section>

<section class="card card-back">
  <svg class="back-graphic" viewBox="0 0 576 329" aria-hidden="true">
    <path d="M 300 0 H 576 V 329 H 300 Q 262 164.5 300 0 Z" fill="var(--brand-blue)"/>
    <path d="M 478 0 H 576 V 329 H 478 Q 548 164.5 478 0 Z" fill="var(--steel-grey)" stroke="var(--card-white)" stroke-width="4"/>
  </svg>

  <div class="back-details">
    <div class="back-wordmark">Veltrano</div>
    <div class="person-name">RUI MATOS</div>
    <div class="person-role">MANAGER</div>
    <div class="address">Rua das Oficinas, 42<br>Postal code: 1200-340 Lisboa</div>
    <ul class="contact-list">
      <li>
        <svg class="contact-icon" viewBox="0 0 24 24"><path d="M6.6 10.8a15.1 15.1 0 0 0 6.6 6.6l2.2-2.2a1 1 0 0 1 1-.25 11.4 11.4 0 0 0 3.6.57 1 1 0 0 1 1 1V20a1 1 0 0 1-1 1A17 17 0 0 1 3 4a1 1 0 0 1 1-1h3.5a1 1 0 0 1 1 1c0 1.25.2 2.45.57 3.6a1 1 0 0 1-.25 1z"/></svg>
        +351 912 480 375
      </li>
      <li>
        <svg class="contact-icon" viewBox="0 0 24 24"><path d="M7 1h10a2 2 0 0 1 2 2v18a2 2 0 0 1-2 2H7a2 2 0 0 1-2-2V3a2 2 0 0 1 2-2zm0 3v14h10V4zm5 15.2a1.2 1.2 0 1 0 0 2.4 1.2 1.2 0 0 0 0-2.4z"/></svg>
        +351 213 570 964
      </li>
      <li>
        <svg class="contact-icon" viewBox="0 0 24 24"><path d="M2 5h20v14H2zm2 2v.5l8 5 8-5V7zm0 2.8V17h16V9.8l-8 5z"/></svg>
        veltrano.oficina@mail.pt
      </li>
      <li>
        <span class="social-square"></span>| veltrano
      </li>
    </ul>
  </div>
</section>

</body>
</html>
```